Property refurbishment & maintenance Business Card Design

Velmorin Ltd is a leading provider of domestic maintenance, building and refurbishment services. Founded in October 2009 by Piotr Velmorin, we aim to provide our customers with exceptional home improvement and maintenance services whilst minimising the disruption and stress caused.
The building services we provide are of the very highest quality. We provide all of your customers with the peace of mind in knowing that they are dealing with experts in construction, renovation and decoration. This is because we are members of the Guild of Craft Contractors (GCC). We have also had our credentials verified by Surelink and the UK government's Keel Seal scheme.
Target Market(s)
Private home owners,letting agents,tenants
Industry/Entity Type
Home Improvement
Contact Information for Business Card
Velmorin ltd.
Piotr Velmorin
14 Pellham Birch Lane ,Ashmere Cross,Fernshire,QX7 2QR,T.01707318257 M:07924168330
E. info@velmorin.example. www.velmorin.example
Look and feel
Each slider illustrates characteristics of the customer's brand and the style your logo design should communicate.

```html
<!DOCTYPE html>
<html lang="en">
<head>
<meta charset="utf-8">
<title>Velmorin Ltd – Business Card</title>
<link rel="stylesheet" href="https://fonts.googleapis.com/css2?family=Tinos:ital,wght@0,400;0,700;1,400&display=swap">
<style>
  :root {
    --bg: #e9e6e1;
    --card: #ffffff;
    --photo-dark: #4a4846;
    --photo-mid: #8d8a86;
    --photo-light: #c9c6c1;
    --white: #ffffff;
    --gold: #b8963f;
    --gold-dark: #8f7230;
    --teal: #3f8c86;
    --grey: #8a8a8a;
    --ink: #4d4d4d;
  }
  * { box-sizing: border-box; margin: 0; padding: 0; }
  html, body { width: 1200px; height: 900px; overflow: hidden; }
  body {
    background: var(--bg);
    font-family: "Tinos", "Times New Roman", serif;
    position: relative;
  }
  .card {
    position: absolute;
    width: 520px;
    height: 336px;
    border-radius: 18px;
    overflow: hidden;
    box-shadow: 0 6px 18px rgba(0,0,0,.18);
  }

  /* Front */
  .card--front { left: 70px; top: 150px; }
  .front-photo {
    position: absolute; inset: 0;
    background: linear-gradient(120deg, var(--photo-light) 0%, var(--photo-mid) 45%, var(--photo-dark) 100%);
  }
  .front-shade { position: absolute; inset: 0; background: rgba(40,38,36,.35); }
  .front-brand { position: absolute; left: 40px; top: 30px; color: var(--white); }
  .brand-name {
    display: flex; align-items: center; gap: 8px;
    font-size: 30px; letter-spacing: 3px; font-weight: 400; line-height: 1;
  }
  .brand-mark { width: 10px; height: 10px; background: currentColor; }
  .brand-tag { font-size: 7.5px; letter-spacing: 1px; margin-top: 4px; padding-left: 18px; white-space: nowrap; }
  .services-rule {
    position: absolute; left: 30px; right: 30px; top: 168px;
    display: flex; align-items: center; gap: 12px; color: var(--white);
  }
  .services-rule .line { flex: 1; height: 1px; background: var(--white); }
  .services-title { font-size: 19px; letter-spacing: 1.5px; line-height: 22px; }
  .service-list {
    position: absolute; list-style: none; color: var(--white);
    font-style: italic; font-size: 17px; line-height: 23px;
  }
  .service-list li { display: flex; align-items: center; gap: 8px; white-space: nowrap; }
  .service-list li::before {
    content: ""; width: 7px; height: 7px; border-radius: 50%; background: var(--white); flex: none;
  }
  .service-list--left { left: 40px; top: 204px; }
  .service-list--right { right: 40px; top: 94px; text-align: right; }
  .service-list--right li { flex-direction: row-reverse; }
  .front-web { position: absolute; right: 40px; bottom: 22px; color: var(--white); font-size: 17px; letter-spacing: .5px; }

  /* Back */
  .card--back { left: 610px; top: 430px; background: var(--card); }
  .back-swoosh { position: absolute; left: 0; bottom: 0; width: 520px; height: 170px; }
  .badges { position: absolute; left: 26px; top: 26px; display: flex; gap: 6px; align-items: center; }
  .badge { display: block; }
  .badge--wide { width: 66px; height: 26px; border: 1.5px solid #c33; border-radius: 3px; }
  .badge--mark { width: 60px; height: 26px; background: #c23a3a; border-radius: 3px; }
  .badge--round { width: 30px; height: 30px; border-radius: 50%; background: #2b4da0; }
  .badge--small { width: 22px; height: 30px; background: #d04040; border-radius: 3px; }
  .back-brand { position: absolute; left: 34px; top: 130px; color: var(--teal); }
  .back-brand .brand-tag { color: var(--gold); }
  .divider { position: absolute; left: 265px; top: 34px; width: 1px; height: 140px; background: linear-gradient(var(--white), #c8c8c8, var(--white)); }
  .contact { position: absolute; left: 290px; top: 30px; color: var(--teal); font-size: 13.5px; line-height: 16px; }
  .contact-name { color: var(--gold); font-weight: 700; font-size: 16px; }
  .contact-role { margin-bottom: 18px; }
  .contact-address { margin-bottom: 16px; white-space: nowrap; }
  .contact-lines { list-style: none; }
  .contact-lines li { display: flex; align-items: center; gap: 10px; }
  .contact-lines svg { width: 13px; height: 13px; fill: var(--gold); flex: none; }
</style>
</head>
<body>

<section class="card card--front" aria-label="Business card front">
  <div class="front-photo" role="img" aria-label="Photograph of tradespeople decorating and repairing a home interior"></div>
  <div class="front-shade"></div>
  <div class="front-brand">
    <div class="brand-name"><span class="brand-mark"></span>VELMORIN</div>
    <div class="brand-tag">PROPERTY REFURBISHMENT &amp; MAINTENANCE</div>
  </div>
  <ul class="service-list service-list--right">
    <li>Decorating Specialists</li>
    <li>Domestic Building</li>
    <li>Electrics, Plumbing and Heating</li>
  </ul>
  <div class="services-rule">
    <span class="line"></span><span class="services-title">SERVICES</span><span class="line"></span>
  </div>
  <ul class="service-list service-list--left">
    <li>Maintenance</li>
    <li>Home Refurbishments</li>
    <li>Kitchens and Bathrooms</li>
  </ul>
  <div class="front-web">www.velmorin.example</div>
</section>

<section class="card card--back" aria-label="Business card back">
  <svg class="back-swoosh" viewBox="0 0 520 170" preserveAspectRatio="none" aria-hidden="true">
    <defs>
      <linearGradient id="goldBand" x1="0" y1="0" x2="0" y2="1">
        <stop offset="0" stop-color="#d4b56a"/>
        <stop offset="1" stop-color="#8f7230"/>
      </linearGradient>
    </defs>
    <path d="M0 120 Q260 150 520 0 L520 30 Q280 175 0 132 Z" fill="#8a8a8a"/>
    <path d="M0 140 Q280 185 520 40 L520 170 L0 170 Z" fill="url(#goldBand)"/>
    <path d="M0 134 Q280 180 520 32" fill="none" stroke="#fff" stroke-width="3"/>
  </svg>
  <div class="badges" aria-label="Membership badges">
    <span class="badge badge--wide"></span>
    <span class="badge badge--mark"></span>
    <span class="badge badge--round"></span>
    <span class="badge badge--small"></span>
  </div>
  <div class="back-brand">
    <div class="brand-name"><span class="brand-mark"></span>VELMORIN</div>
    <div class="brand-tag">PROPERTY REFURBISHMENT &amp; MAINTENANCE</div>
  </div>
  <div class="divider"></div>
  <div class="contact">
    <div class="contact-name">Piotr Velmorin</div>
    <div class="contact-role">Managing Director</div>
    <div class="contact-address">14 Pellham Birch Lane,<br>Ashmere Cross, Fernshire, QX7 2QR</div>
    <ul class="contact-lines">
      <li><svg viewBox="0 0 16 16"><path d="M2 5c0-2 2-3 6-3s6 1 6 3l-3 1-1-2H6L5 6 2 5zm2 3h8l1 6H3l1-6zm4 1.5a2 2 0 1 0 0 4 2 2 0 0 0 0-4z"/></svg>017 0731 8257</li>
      <li><svg viewBox="0 0 16 16"><path d="M4 1h8v14H4zM5.5 3v9h5V3zM8 13a.8.8 0 1 0 0 .1z"/></svg>079 2416 8330</li>
      <li><svg viewBox="0 0 16 16"><path d="M1 3h14v10H1zm1.5 1.5L8 9l5.5-4.5z"/></svg>info@velmorin.example</li>
      <li><svg viewBox="0 0 16 16"><path d="M8 1a7 7 0 1 0 0 14A7 7 0 0 0 8 1zm-1 2.2V7H3.1A5 5 0 0 1 7 3.2zM9 3.2A5 5 0 0 1 12.9 7H9zM3.1 9H7v3.8A5 5 0 0 1 3.1 9zM9 9h3.9A5 5 0 0 1 9 12.8z"/></svg>www.velmorin.example</li>
    </ul>
  </div>
</section>

</body>
</html>
```